Rack Card for Charter Sail Boat business in SF Bay

We are in need of a rack card design to highlight the business to tourists and locals. 2 sided card 3.86" x 8.39" (full bleed)

We are looking for visually appleaing designs on the front and back but a little more detail on the back.

Use the info provided (text and info) on the website to include the 3 key services (Quick, 1/2 day, fullday) and aspects of the boat, location and other key info for customers (not prices). DO NOT INCLUDE ALL THIS TEXT please pick the elements you would like to fit your design and inform the customer as you would like about the business.

I can also provide photos directly from the video if you think those would fit your design. If video doesn't work on this upload you can view it at the website or facebook page (www.fb.com/tidewrenllc)

Now included a few video pictures in files for your use

Target Market(s)

Tourists and locals to san francisco east bay. 25 - 55 years old. Men and women.

Industry/Entity Type

Entertainment

Colors
0455a3
ec1f27
f3f1f8

Requirements
Must have
• Highlight services, key contact information (email, phone, website site), Visual impact
• 2-sided card - 3.86" x 8.39" (98 x 213 mm)
Nice to have
• facebook link, electric engine(green),

```html
<!DOCTYPE html>
<html lang="en">
<head>
<meta charset="utf-8">
<title>Tidewren Rack Card</title>
<link href="https://fonts.googleapis.com/css2?family=Arvo:wght@400;700&family=Raleway:wght@400;500;600&display=swap" rel="stylesheet">
<style>
  :root {
    --brand-blue: #0455a3;
    --deep-blue: #033f7e;
    --light-blue: #1d74cf;
    --brand-red: #ec1f27;
    --paper: #f3f1f8;
    --white: #ffffff;
    --grey-stripe: #c9cdd6;
    --canvas: #e4e6ea;
  }
  * { margin: 0; padding: 0; box-sizing: border-box; }
  html, body { width: 1184px; height: 1200px; overflow: hidden; background: var(--canvas); }
  .stage { position: relative; width: 1184px; height: 1200px; }

  .rack-card {
    position: absolute; top: 121px; width: 444px; height: 958px;
    overflow: hidden; background: var(--brand-blue);
    font-family: "Raleway", sans-serif; color: var(--white);
  }
  .rack-card--front { left: 125px; }
  .rack-card--back { left: 615px; }
  .card-shapes { position: absolute; inset: 0; }

  .brand-name {
    position: absolute; font-family: "Arvo", serif; font-weight: 400;
    color: var(--white); letter-spacing: 1px;
  }
  .rack-card--front .brand-name { left: 222px; top: 52px; font-size: 40px; }
  .rack-card--back .brand-name { left: 40px; top: 282px; font-size: 42px; }

  .license-seal {
    position: absolute; left: 29px; top: 41px; width: 74px; height: 74px;
    border-radius: 50%; background: var(--deep-blue); border: 4px solid #e6b325;
  }

  .snapshot {
    position: absolute; background: var(--white); padding: 8px 8px 22px;
    box-shadow: 0 3px 8px rgba(0,0,0,.35);
  }
  .snapshot__photo { width: 100%; height: 100%; }
  .snapshot__pin {
    position: absolute; top: -4px; right: 6px; width: 12px; height: 12px;
    border-radius: 50%; background: var(--brand-red);
  }

  .front-headline {
    position: absolute; left: 180px; width: 226px; top: 444px; text-align: center;
    font-family: "Arvo", serif; font-size: 19px; line-height: 31px; letter-spacing: .5px;
  }
  .feature-checks {
    position: absolute; right: 44px; top: 509px; list-style: none; text-align: right;
    font-family: "Arvo", serif; font-size: 15px; line-height: 20px; color: var(--brand-red);
  }
  .feature-checks svg { width: 12px; height: 10px; margin-left: 6px; }
  .front-intro {
    position: absolute; left: 25px; width: 394px; top: 606px; text-align: center;
    font-size: 16px; line-height: 20.5px; font-weight: 500;
  }
  .front-body {
    position: absolute; left: 25px; width: 390px; top: 674px; text-align: justify;
    font-size: 12.5px; line-height: 15.4px;
  }
  .booking-button {
    position: absolute; left: 67px; top: 846px; width: 298px; height: 40px;
    border-radius: 20px; background: var(--brand-red); color: var(--white);
    font-family: "Raleway", sans-serif; font-weight: 600; font-size: 15.5px;
    display: flex; align-items: center; justify-content: center;
    box-shadow: 0 3px 5px rgba(0,0,0,.3);
  }

  .contact-block {
    position: absolute; left: 0; width: 444px; top: 896px; text-align: center;
    font-family: "Arvo", serif; color: var(--brand-red); font-size: 15.5px; line-height: 26px;
    font-style: normal;
  }

  .tagline {
    position: absolute; left: 17px; top: 374px; font-family: "Arvo", serif;
    font-size: 14.5px; color: var(--brand-red);
  }
  .services-tab {
    position: absolute; left: 0; top: 408px; width: 241px; height: 40px;
    background: var(--brand-red); border-radius: 0 20px 20px 0;
    font-family: "Arvo", serif; font-size: 19px; font-weight: 400; letter-spacing: .5px;
    display: flex; align-items: center; padding-left: 18px;
    box-shadow: 0 3px 5px rgba(0,0,0,.3);
  }
  .service { position: absolute; left: 19px; }
  .service__title { font-family: "Arvo", serif; font-size: 19px; font-weight: 400; line-height: 24px; }
  .service__text { font-size: 13px; line-height: 15.5px; margin-top: 2px; }
  .service--blast { top: 457px; width: 268px; }
  .service--half { top: 557px; width: 268px; }
  .service--full { top: 656px; width: 410px; }
  .service--custom { top: 725px; width: 410px; }

  .route-map {
    position: absolute; top: 797px; width: 102px; height: 102px; border-radius: 50%;
    border: 4px solid var(--white); background: radial-gradient(circle at 45% 40%, #dfe9f1, #b7cfe3);
    box-shadow: 0 3px 6px rgba(0,0,0,.3);
  }
</style>
</head>
<body>
<main class="stage">

  <section class="rack-card rack-card--front">
    <svg class="card-shapes" width="444" height="958" viewBox="0 0 444 958">
      <defs>
        <linearGradient id="frontBlue" x1="0" y1="0" x2="0" y2="1">
          <stop offset="0" stop-color="#1266c0"/>
          <stop offset="1" stop-color="#0455a3"/>
        </linearGradient>
        <linearGradient id="sunsetTones" x1="0" y1="0" x2="0" y2="1">
          <stop offset="0" stop-color="#6d86a6"/>
          <stop offset=".45" stop-color="#e7a04d"/>
          <stop offset=".55" stop-color="#5a5560"/>
          <stop offset="1" stop-color="#1f2a3a"/>
        </linearGradient>
      </defs>
      <rect width="444" height="958" fill="url(#frontBlue)"/>
      <path d="M0,196 C130,150 300,190 444,100 L444,388 C350,430 240,340 0,372 Z" fill="url(#sunsetTones)" role="img" aria-label="Photo: sunset over the bay seen from the deck of a sailboat"/>
      <path d="M0,196 C130,150 300,190 444,100" fill="none" stroke="var(--grey-stripe)" stroke-width="10"/>
      <path d="M0,190 C130,144 300,184 444,94" fill="none" stroke="#ffffff" stroke-width="4"/>
      <path d="M0,372 C240,340 350,430 444,388" fill="none" stroke="var(--grey-stripe)" stroke-width="10"/>
      <path d="M0,380 C240,348 350,438 444,396" fill="none" stroke="#ffffff" stroke-width="4"/>
      <path d="M0,866 C150,836 300,828 444,852 L444,958 L0,958 Z" fill="#ffffff"/>
      <path d="M0,858 C150,828 300,820 444,844" fill="none" stroke="var(--grey-stripe)" stroke-width="6"/>
    </svg>

    <div class="license-seal" aria-hidden="true"></div>
    <div class="brand-name">Tidewren</div>

    <figure class="snapshot" style="left:9px;top:338px;width:150px;height:137px;transform:rotate(-4deg);">
      <div class="snapshot__photo" role="img" aria-label="Photo: sailboat deck with the city skyline" style="background:linear-gradient(#8fb1d3,#43607f);"></div>
      <span class="snapshot__pin"></span>
    </figure>
    <figure class="snapshot" style="left:37px;top:432px;width:136px;height:136px;transform:rotate(6deg);">
      <div class="snapshot__photo" role="img" aria-label="Photo: children in life jackets aboard the boat" style="background:linear-gradient(#4b6d95,#2c3550);"></div>
      <span class="snapshot__pin"></span>
    </figure>

    <h1 class="front-headline" style="font-weight:400;">ULTIMATE EAST BAY SAILBOAT CHARTER</h1>
    <ul class="feature-checks">
      <li>Modern<svg viewBox="0 0 12 10"><path d="M1,5 L4.5,8.5 L11,1.5" fill="none" stroke="#ec1f27" stroke-width="2"/></svg></li>
      <li>Entertaining<svg viewBox="0 0 12 10"><path d="M1,5 L4.5,8.5 L11,1.5" fill="none" stroke="#ec1f27" stroke-width="2"/></svg></li>
      <li>Safe<svg viewBox="0 0 12 10"><path d="M1,5 L4.5,8.5 L11,1.5" fill="none" stroke="#ec1f27" stroke-width="2"/></svg></li>
    </ul>

    <p class="front-intro">Come enjoy an amazing experience aboard TideWren and view San Francisco and the rest of the bay as so few are able to do.</p>
    <p class="front-body">TideWren is a supreme blue-water cruising boat with all the modern safety, comfort and entertainment equipment you would expect. Your time aboard TideWren is yours to enjoy and direct as you wish while we show you San Francisco Bay, the Golden Gate Bridge, Alcatraz, Treasure and Angel Islands and so much more. Come join us and share the wonders around San Francisco Bay with your friends and family. We love to show families how to sail and have great fun on the water while staying safe.</p>

    <div class="booking-button">NOW ACCEPTING BOOKINGS!</div>
    <address class="contact-block">
      <div>Call: (510) 555-SAIL (7245)</div>
      <div>Bookings@TideWren.com &nbsp;|&nbsp; www.tidewren.com</div>
    </address>
  </section>

  <section class="rack-card rack-card--back">
    <svg class="card-shapes" width="444" height="958" viewBox="0 0 444 958">
      <defs>
        <linearGradient id="backBlue" x1="0" y1="0" x2="0" y2="1">
          <stop offset="0" stop-color="#1266c0"/>
          <stop offset="1" stop-color="#0455a3"/>
        </linearGradient>
        <linearGradient id="deckTones" x1="0" y1="0" x2="0" y2="1">
          <stop offset="0" stop-color="#3f79c6"/>
          <stop offset=".45" stop-color="#8fb3dc"/>
          <stop offset=".55" stop-color="#3a5f86"/>
          <stop offset="1" stop-color="#6c5a4a"/>
        </linearGradient>
      </defs>
      <rect width="444" height="958" fill="url(#backBlue)"/>
      <path d="M0,0 H444 V300 C300,230 120,200 0,262 Z" fill="url(#deckTones)" role="img" aria-label="Photo: view forward over the helm and deck toward the bay"/>
      <path d="M0,262 C120,200 300,230 444,300" fill="none" stroke="var(--grey-stripe)" stroke-width="10"/>
      <path d="M0,254 C120,192 300,222 444,292" fill="none" stroke="#ffffff" stroke-width="4"/>
      <path d="M0,880 C150,850 300,842 444,866 L444,958 L0,958 Z" fill="#ffffff"/>
      <path d="M0,872 C150,842 300,834 444,858" fill="none" stroke="var(--grey-stripe)" stroke-width="6"/>
    </svg>

    <div class="brand-name">Tidewren</div>

    <figure class="snapshot" style="left:312px;top:165px;width:132px;height:140px;transform:rotate(5deg);">
      <div class="snapshot__photo" role="img" aria-label="Photo: sailboat moored at the marina" style="background:linear-gradient(#4a86d0,#5b6470);"></div>
      <span class="snapshot__pin"></span>
    </figure>
    <figure class="snapshot" style="left:302px;top:309px;width:142px;height:146px;transform:rotate(-4deg);">
      <div class="snapshot__photo" role="img" aria-label="Photo: deck and bow of the sailboat under way" style="background:linear-gradient(#c7d3de,#3d4c5c);"></div>
      <span class="snapshot__pin"></span>
    </figure>
    <figure class="snapshot" style="left:312px;top:466px;width:132px;height:180px;transform:rotate(8deg);">
      <div class="snapshot__photo" role="img" aria-label="Photo: white sail filled with wind" style="background:linear-gradient(#e9edf2,#7f96ad);"></div>
      <span class="snapshot__pin"></span>
    </figure>

    <p class="tagline">Modern • Entertaining • Safe</p>
    <h2 class="services-tab">SERVICES OFFERED</h2>

    <article class="service service--blast">
      <h3 class="service__title">2 HOUR BLAST</h3>
      <p class="service__text">Could be a sunset sail, an early morning wake up cruise or a blast out into the bay anytime to find peace, fresh air and amazing views.</p>
    </article>
    <article class="service service--half">
      <h3 class="service__title">1/2 DAY FUN</h3>
      <p class="service__text">A full morning, afternoon or evening out in the Bay seeing many of the main features and landmarks close to the Bay from the water. Actual duration 4-5 hours anchor.</p>
    </article>
    <article class="service service--full">
      <h3 class="service__title">FULL DAY ADVENTURE</h3>
      <p class="service__text">The day includes a complete circuit of the Bay and lunch at anchor. Actual duration 7-8 hours</p>
    </article>
    <article class="service service--custom">
      <h3 class="service__title">CUSTOM CRUISES</h3>
      <p class="service__text">If your looking for something a little different or to mix it up a bit, let us know and we can make it happen.</p>
    </article>

    <div class="route-map" style="left:63px;" role="img" aria-label="Map: 2 hour blast sailing route"></div>
    <div class="route-map" style="left:178px;" role="img" aria-label="Map: half day sailing route"></div>
    <div class="route-map" style="left:292px;" role="img" aria-label="Map: full day sailing route"></div>

    <address class="contact-block">
      <div>Call: (510) 555-SAIL (7245)</div>
      <div>Bookings@TideWren.com &nbsp;|&nbsp; www.tidewren.com</div>
    </address>
  </section>

</main>
</body>
</html>
```